Management Consultancy needs sharp professional services showcased in a brochure

We are a management consultancy specializing on contract management and conflict avoidance services requiring a professional brochure showcasing our services to prospective clients.

Attached are a selection of existing stationary and the colour scheme.

Further details on our company can be found at www.velto-advisory-partners.com
Updates

Preference is for bi-fold, however, innovative tri-fold will be considered. Added Monday, August 7, 2017

Target Market(s)

Construction companies, consultants, developers, oil and gas service providers, NGO's, SME's.

Industry/Entity Type

Management

Requirements
Must have
• High degree of professionalism with eye catching, sharp detail. No frils.
• Colour scheme as per the attachments
• Font as per attachments - Century Gothic
• Details of our company and services
Nice to have
• Open to ideas, thinking along the lines of a car brochure type design.
• Bi-fold preferred, by trifold accepted if innovative.
Should not have
• Remove reference to the United Arab Emirates.
• No cartoon/clipart photos.

```html
<!DOCTYPE html>
<html lang="en">
<head>
<meta charset="utf-8">
<title>Velto Advisory – Contract and Conflict Advisory Brochure</title>
<link href="https://fonts.googleapis.com/css2?family=Montserrat:ital,wght@0,400;0,600;0,700;1,700;1,800&family=Questrial&display=swap" rel="stylesheet">
<style>
:root{
  --navy:#27364c;
  --navy-soft:#33445d;
  --red:#bf272d;
  --page:#ececed;
  --ink:#2e3a4a;
  --muted:#8c939c;
  --outline:#b4b8be;
  --bg:#ffffff;
}
*{margin:0;padding:0;box-sizing:border-box}
html,body{width:1200px;height:454px;overflow:hidden;background:var(--bg)}
body{font-family:"Questrial",sans-serif;color:var(--ink)}
.stage{position:relative;width:1200px;height:454px}
.spread{position:absolute;top:38px;height:362px;overflow:hidden}
.spread--cover{left:46px;width:530px}
.spread--services{left:622px;width:532px;background:var(--page)}
.abs{position:absolute}
.photo{position:absolute;background:linear-gradient(135deg,#cfd1d4,#7d8288)}
.photo--dark{background:linear-gradient(135deg,#5b6068,#1f2227)}
.photo--desk{background:linear-gradient(160deg,#bfb7ad 0%,#8a8680 45%,#4a4f57 100%)}

/* cover */
.tagline{position:absolute;left:0;top:24px;width:234px;text-align:right;font-family:"Montserrat",sans-serif;font-size:11.5px;line-height:12.5px;color:#4a5870}
.tagline b{color:#6d7a8f;font-weight:700}
.tagline .final{color:#8793a5}
.tagline .final b{color:#a7b0bd}
.title-block{position:absolute;left:410px;top:106px;text-align:right;font-family:"Montserrat",sans-serif;font-weight:700;color:var(--red)}
.title-block span{display:inline-block;background:rgba(39,54,76,.82);padding:1px 6px;font-size:16px;line-height:19px;margin-top:2px}
.title-block small{color:#fff;font-weight:400;font-size:9px;margin-right:2px}
.countries{position:absolute;left:8px;top:302px;font-family:"Montserrat",sans-serif;font-size:5px;font-weight:700;letter-spacing:.3px;color:#fff}
.countries i{font-style:normal;color:var(--red);margin:0 3px}
.rule{position:absolute;left:8px;top:312px;width:250px;height:.7px;background:#8793a5}
.contact{position:absolute;left:8px;top:318px;font-size:5.2px;color:#fff}
.brand{position:absolute;left:360px;top:268px;display:flex;align-items:center;gap:6px;font-family:"Montserrat",sans-serif;font-weight:600;font-size:15px;letter-spacing:.5px;color:var(--navy)}
.brand .dot{width:9px;height:9px;border-radius:50%;background:var(--red)}
.web{position:absolute;left:376px;top:312px;font-size:7px;color:var(--navy)}

/* services */
.h-section{position:absolute;font-family:"Montserrat",sans-serif;font-weight:700;font-size:10px;color:var(--red)}
.intro{position:absolute;font-size:3.6px;line-height:4.6px;color:var(--muted)}
.h-item{position:absolute;font-family:"Montserrat",sans-serif;font-weight:700;font-style:italic;font-size:5.8px;line-height:6.2px;color:var(--ink);white-space:nowrap}
.body{position:absolute;font-size:3.4px;line-height:4.4px;color:var(--muted)}
.body p{margin-bottom:2.5px}
.body ul{list-style:none}
.body li{position:relative;padding-left:4px;margin-bottom:1.5px}
.body li::before{content:"›";position:absolute;left:0;color:var(--red)}
</style>
</head>
<body>
<div class="stage">

  <!-- Cover spread -->
  <section class="spread spread--cover">
    <svg class="abs" width="530" height="362" viewBox="0 0 530 362" style="left:0;top:0">
      <rect x="265" y="0" width="265" height="362" fill="#fff"/>
      <rect x="0" y="0" width="265" height="362" fill="var(--navy)"/>
      <path d="M40 0 Q150 110 110 362" fill="none" stroke="var(--navy-soft)" stroke-width="60" opacity=".45"/>
      <path d="M150 0 Q240 120 265 260" fill="none" stroke="var(--red)" stroke-width="28" opacity=".18"/>
    </svg>
    <div class="photo photo--desk" role="img" aria-label="Photo of a business meeting at a desk with hands over documents" style="left:265px;top:0;width:265px;height:240px"></div>
    <svg class="abs" width="265" height="362" viewBox="0 0 265 362" style="left:265px;top:0">
      <path d="M0 230 Q110 150 265 180 L265 206 Q120 185 0 270 Z" fill="var(--navy)"/>
      <path d="M0 232 Q110 168 265 198 L265 210 Q120 196 0 262 Z" fill="var(--red)"/>
      <path d="M0 262 Q120 196 265 210 L265 362 L0 362 Z" fill="#fff"/>
    </svg>

    <p class="tagline">better <b>engagements</b><br>better <b>awareness</b><br>better <b>performance</b><br><span class="final">.......<b>better value</b></span></p>

    <div class="title-block">
      <span><small>The</small>Contract</span><br>
      <span><small>and</small>Conflict</span><br>
      <span>Advisory</span>
    </div>

    <p class="countries">UNITED KINGDOM<i>•</i>IRELAND<i>•</i>BRAZIL</p>
    <div class="rule"></div>
    <p class="contact">Velto Advisory Limited · E: info@velto-advisory-partners.com · www.<b>velto-advisory-partners</b>.com</p>

    <div class="brand"><span class="dot"></span>VELTO ADVISORY</div>
    <p class="web">www.<b>velto-advisory-partners</b>.com</p>
  </section>

  <!-- Services spread -->
  <section class="spread spread--services">
    <svg class="abs" width="532" height="362" viewBox="0 0 532 362" style="left:0;top:0">
      <path d="M110 40 Q20 160 60 362" fill="none" stroke="var(--red)" stroke-width="34" opacity=".08"/>
      <path d="M-20 60 Q40 200 10 362" fill="none" stroke="var(--navy)" stroke-width="20" opacity=".06"/>
      <text x="14" y="62" textLength="506" lengthAdjust="spacingAndGlyphs" font-family="Montserrat, sans-serif" font-weight="800" font-style="italic" font-size="70" fill="var(--outline)">Our Services</text>
    </svg>

    <!-- Conflict Advisory -->
    <h2 class="h-section" style="left:16px;top:70px">Conflict Advisory</h2>
    <p class="intro" style="left:16px;top:83px;width:228px">Every contract has the ability to be settled; it is on this premise we deliver effective solutions to contractual and commercial disputes with the aim of preserving the relationships and strengthening the parties for the future ahead.</p>

    <div class="photo" role="img" aria-label="Puzzle pieces" style="left:16px;top:98px;width:76px;height:22px;background:linear-gradient(135deg,#f2f2f2,#9a9da2)"></div>
    <div class="photo photo--dark" role="img" aria-label="Handshake" style="left:122px;top:98px;width:80px;height:36px"></div>

    <h3 class="h-item" style="left:16px;top:124px">Restoration and<br>Mediation Services</h3>
    <div class="body" style="left:16px;top:139px;width:100px">
      <p>Providing advocacy in the field of general commercial and contract issues, real estate, construction, property, civil engineering and vessel, ship and rig, and related services including aviation, chartering, media services and purchases.</p>
      <p>Providing effective restoration methods, achieving a mutually acceptable outcome in all phases of the contract cycle, ensuring all parties remain diligent, more committed and accountable for the progress of the transaction and relationship.</p>
    </div>

    <h3 class="h-item" style="left:122px;top:139px">Negotiation Support<br>Services</h3>
    <div class="body" style="left:122px;top:154px;width:100px">
      <p>Ensuring success in negotiation, we aim to provide direction to negotiators in the early stages of conflict in order to avert escalation and to reduce conflict aftermath.</p>
      <p>Through assessment of relationships, perception and conflict strategy we ensure adequate negotiation preparation and guidance with the increased outcome of a win-win for all parties.</p>
    </div>

    <div class="photo" role="img" aria-label="Open book pages in soft light" style="left:16px;top:210px;width:76px;height:32px;background:linear-gradient(135deg,#e6e6e6,#6d7177)"></div>
    <div class="photo" role="img" aria-label="Stacked documents on a desk" style="left:122px;top:210px;width:80px;height:36px;background:linear-gradient(135deg,#f0f0f0,#b5b8bc)"></div>

    <h3 class="h-item" style="left:16px;top:254px">Shuttle Diplomacy<br>and In Persona<br>Intermediary<br>Services</h3>
    <div class="body" style="left:16px;top:284px;width:100px">
      <p>Providing a presence in disputes and processes where parties are:</p>
      <p>(a) unable to attend or</p>
      <p>(b) unwilling to attend.</p>
      <p>Additionally providing a neutral platform for documentation submission review and filing, adding vetting and response in shuttle diplomacy.</p>
    </div>

    <h3 class="h-item" style="left:122px;top:250px">Workplace /<br>Corporate<br>Mediation<br>Services</h3>
    <div class="body" style="left:166px;top:250px;width:72px">
      <p>Providing effective resolution to workplace misunderstandings, personality conflicts, co-operation and opinion differences, with the objective of increasing workplace performance and reducing management and HR resource deployment.</p>
    </div>

    <!-- Contract Advisory -->
    <h2 class="h-section" style="left:302px;top:70px">Contract Advisory</h2>
    <p class="intro" style="left:302px;top:83px;width:222px">Effective contract management delivered through our Contract Advisory ensures that the contract is an effective asset not a tool. Through review, planning and effective application, we ensure that contractual obligations are maintained and risks are mitigated through the full contract life cycle providing the optimum contractual engagement.</p>

    <div class="photo" role="img" aria-label="Contract document pages" style="left:298px;top:102px;width:24px;height:38px;background:linear-gradient(135deg,#fafafa,#c4c6c9)"></div>
    <h3 class="h-item" style="left:326px;top:102px">Contract Trouble-shooting</h3>
    <div class="body" style="left:326px;top:110px;width:84px">
      <ul>
        <li>Contract Troubleshooting including drafting and interpretation assistance via our 'Recovered' protocol.</li>
        <li>Providing secondary review, analysis and interpretation with reporting on application of clauses including scenario dissection aiding the deconstruction of terms to reveal the true meaning and implications.</li>
        <li>Contract Workshops with key stakeholders enabling a harmonised understanding of contractual obligations enabling a clear procedure establishment.</li>
      </ul>
    </div>

    <div class="photo photo--dark" role="img" aria-label="Chess pieces on a board" style="left:442px;top:98px;width:72px;height:36px"></div>
    <h3 class="h-item" style="left:416px;top:140px">Strategic Review &amp;<br>Contract Risk<br>Assessment</h3>
    <div class="body" style="left:416px;top:160px;width:106px">
      <ul>
        <li>Advisory of current contract application suitability.</li>
        <li>Steering guidance and contract assessment advisory.</li>
        <li>Contract audit and optimisation assessments.</li>
        <li>Development of internal contract management and administration policy and procedures.</li>
        <li>Contract management planning – Advisory at all phases of the contract Life Cycle ('CLC').</li>
      </ul>
    </div>

    <div class="photo" role="img" aria-label="Signing a tender document" style="left:298px;top:190px;width:20px;height:20px;background:linear-gradient(135deg,#e2e2e2,#8a8d92)"></div>
    <h3 class="h-item" style="left:322px;top:190px">Tender Review<br>&amp; Bid Support</h3>
    <div class="body" style="left:322px;top:205px;width:84px">
      <ul>
        <li>Guidance in tender review (both received and issued).</li>
        <li>RFQ and RFP drafting and review.</li>
      </ul>
    </div>

    <div class="photo" role="img" aria-label="Hands at a laptop keyboard" style="left:442px;top:200px;width:72px;height:26px;background:linear-gradient(135deg,#6f757e,#2a2d33)"></div>
    <h3 class="h-item" style="left:416px;top:232px">Contract Fraud<br>Investigation</h3>
    <div class="body" style="left:464px;top:232px;width:58px">
      <ul>
        <li>Advisory of contract practices which are susceptible to fraudulent activity and investigation of key areas where fraud is suspected.</li>
      </ul>
    </div>

    <h3 class="h-item" style="left:322px;top:236px">Contracts Audit Services<br>&amp; Performance Mgmt.</h3>
    <div class="body" style="left:322px;top:251px;width:84px">
      <ul>
        <li>Audit of contractual mechanisms, compliance and corrective measures on deficiencies.</li>
        <li>Advisory and guidance for corrective measures including performance management and establishment and monitoring of key performance indicators ('KPI's').</li>
        <li>Contract harmonisation and benchmarking.</li>
        <li>Post contract closeout review and administration guidance and contract management planning.</li>
        <li>Third party contract auditing including PMC / PMT process review for major and minor projects.</li>
      </ul>
    </div>

    <div class="photo" role="img" aria-label="Calculator and pen on paperwork" style="left:292px;top:266px;width:26px;height:48px;background:linear-gradient(135deg,#f4f4f4,#a9acb0)"></div>

    <div class="photo" role="img" aria-label="Hands working on a tablet at a desk" style="left:442px;top:262px;width:72px;height:24px;background:linear-gradient(135deg,#5e646c,#24272c)"></div>
    <h3 class="h-item" style="left:416px;top:292px">Temporary Placement<br>Contract Management<br>Solutions</h3>
    <div class="body" style="left:416px;top:313px;width:106px">
      <ul>
        <li>Provision of fixed term temporary contract management and contract administration professionals into your organisation to provide immediate on hand contracts management solutions.</li>
      </ul>
    </div>
  </section>

</div>
</body>
</html>
```